Morvex Business Card (intended for Business Card sized magnet)

Hi guys,

I would like to get a design for my business card for the restaurant. The design must be single sided as I intend to produce business card sized magnets.

The File attached must me on and I'm open for new ides

Can you please ensure that the design meets Cardowell's magnetic business card size specifications:

http://www.cardowell.example.au/custom-magnets.aspx?txi=15695&xnid=TopNav_Magnetic+Business+Cards+(linked+item)_Magnets_Marketing+Products&xnav=TopNav

Full Bleed Size (starting document size):
90 x 52 mm
1062 x 615 pixels
* Finished artwork should use the full bleed dimensions for best results.

Document Trim Size (final size after being cut):
87 x 49 mm
1028 x 579 pixels
* Please be sure to keep all text within the safe margin.

Resolution:
300 DPI

The winning design/source files need to meet these specifications.

Thanks
Updates

Hi guys, can I see more options please Thanks

```html
<!DOCTYPE html>
<html lang="en">
<head>
<meta charset="utf-8">
<title>Morvex Business Card</title>
<link rel="stylesheet" href="https://fonts.googleapis.com/css2?family=Alegreya:ital,wght@0,400;1,400&family=Carlito&display=swap">
<style>
  :root {
    --page: #ffffff;
    --card-black: #0e0e0e;
    --panel-grey: #c8c8c8;
    --panel-grey-light: #d2d2d2;
    --ink: #0a0a0a;
    --text-grey: #9c9c9c;
    --icon-grey: #c4c4c4;
    --band-dark: #1d1d1d;
    --band-line: #2c2c2c;
    --band-light: #a6a6a6;
    --ornament-grey: #7a7a7a;
  }
  * { margin: 0; padding: 0; box-sizing: border-box; }
  html, body {
    width: 1200px; height: 1000px; overflow: hidden;
    background: var(--page);
  }
  .canvas { position: relative; width: 1200px; height: 1000px; }
  .card {
    position: absolute; left: 20px; top: 144px;
    width: 1158px; height: 670px;
    background: var(--card-black);
    overflow: hidden;
  }
  .brand-panel {
    position: absolute; left: 682px; top: 0;
    width: 446px; height: 670px;
    background: linear-gradient(160deg, var(--panel-grey-light), var(--panel-grey));
  }
  .brand-name {
    position: absolute; left: 0; top: 148px; width: 446px;
    text-align: center;
    font-family: "Alegreya", Georgia, serif;
    font-weight: 400; font-size: 118px; line-height: 1;
    color: var(--ink);
  }
  .brand-rule {
    position: absolute; left: 0; width: 446px; height: 4px;
    background: var(--ink);
  }
  .brand-rule.top { top: 311px; }
  .brand-rule.bottom { top: 455px; }
  .brand-ornament {
    position: absolute; left: 0; top: 318px; width: 446px; height: 134px;
    background: var(--ornament-grey);
  }
  .footer-band {
    position: absolute; left: 0; top: 558px; width: 1158px; height: 96px;
    border-top: 3px solid var(--band-line);
    border-bottom: 3px solid var(--band-line);
    background: linear-gradient(90deg, var(--band-dark) 0, var(--band-dark) 682px, var(--band-light) 682px, var(--band-light) 1128px, var(--band-dark) 1128px);
  }
  .holder-name {
    position: absolute; left: 45px; top: 90px;
    font-family: "Alegreya", Georgia, serif;
    font-size: 46px; line-height: 1; color: var(--text-grey);
  }
  .holder-title {
    position: absolute; left: 48px; top: 144px;
    font-family: "Alegreya", Georgia, serif;
    font-style: italic; font-size: 32px; line-height: 1; color: var(--text-grey);
  }
  .contact-list {
    position: absolute; left: 40px; top: 334px; list-style: none;
  }
  .contact-item {
    display: flex; align-items: center; height: 46px;
    font-family: "Carlito", Calibri, sans-serif;
    font-size: 27px; color: var(--text-grey);
  }
  .contact-icon { width: 30px; height: 26px; margin-right: 20px; fill: var(--icon-grey); }
</style>
</head>
<body>
<div class="canvas">
  <div class="card">
    <p class="holder-name">L.Varesko</p>
    <p class="holder-title">My Title</p>

    <ul class="contact-list">
      <li class="contact-item">
        <svg class="contact-icon" viewBox="0 0 30 26" aria-hidden="true"><path d="M15 2 L2 13 H6 V24 H12 V17 H18 V24 H24 V13 H28 Z"/><rect x="21" y="3" width="3" height="6"/></svg>
        412, Brennock Rd, Ashvale North, 3188
      </li>
      <li class="contact-item">
        <svg class="contact-icon" viewBox="0 0 30 26" aria-hidden="true"><g fill="none" stroke="var(--icon-grey)" stroke-width="2"><circle cx="15" cy="13" r="11"/><ellipse cx="15" cy="13" rx="5" ry="11"/><line x1="4" y1="13" x2="26" y2="13"/><line x1="6" y1="7" x2="24" y2="7"/><line x1="6" y1="19" x2="24" y2="19"/></g></svg>
        www.morvex.example.au
      </li>
      <li class="contact-item">
        <svg class="contact-icon" viewBox="0 0 30 26" aria-hidden="true"><rect x="2" y="5" width="26" height="17"/><path d="M3 6 L15 15 L27 6" fill="none" stroke="var(--card-black)" stroke-width="2"/></svg>
        morvex412@mailbox.example
      </li>
      <li class="contact-item">
        <svg class="contact-icon" viewBox="0 0 30 26" aria-hidden="true"><path d="M2 9 C2 3 28 3 28 9 V12 H21 V9 H9 V12 H2 Z"/><path d="M8 12 H22 L26 23 H4 Z"/><circle cx="15" cy="17" r="3" fill="var(--card-black)"/></svg>
        03 9000 4821
      </li>
    </ul>

    <div class="brand-panel">
      <p class="brand-name">Morvex</p>
      <div class="brand-rule top"></div>
      <div class="brand-ornament" role="img" aria-label="Decorative interlaced star pattern band with red, teal and yellow accents"></div>
      <div class="brand-rule bottom"></div>
    </div>

    <div class="footer-band" role="img" aria-label="Decorative interlaced star pattern border running along the bottom of the card"></div>
  </div>
</div>
</body>
</html>
```